Lena Corvel Business Card

I need a business card that reflects my current website: itslenacorvel.com and screenshot attached. If we keep the color scheme of the site and sample card below that would be ideal. The business card should include the information on the attached sample cards.

Industry/Entity Type

Business

```html
<!DOCTYPE html>
<html lang="en">
<head>
<meta charset="utf-8">
<title>Lena Corvel Business Card</title>
<link href="https://fonts.googleapis.com/css2?family=Libre+Baskerville:wght@400;700&display=swap" rel="stylesheet">
<style>
  :root {
    --backdrop: #8c8c8c;
    --card: #ffffff;
    --ink: #222222;
    --muted: #6a6a6a;
    --teal: #4fb697;
    --teal-soft: #bfe5d8;
    --grey: #b4b4b4;
  }
  * { margin: 0; padding: 0; box-sizing: border-box; }
  html, body { width: 1200px; height: 874px; overflow: hidden; }
  body {
    background: var(--backdrop);
    font-family: "Libre Baskerville", Georgia, serif;
    color: var(--ink);
    display: flex;
    align-items: center;
    justify-content: center;
    gap: 60px;
  }
  .card {
    width: 520px;
    height: 297px;
    border-radius: 12px;
    background: var(--card);
    position: relative;
    overflow: hidden;
    box-shadow: 0 6px 18px rgba(0,0,0,.25);
  }
  /* Front */
  .card-front .frame {
    position: absolute;
    inset: 0;
  }
  .card-front .content {
    position: absolute;
    inset: 0;
    display: flex;
    flex-direction: column;
    align-items: center;
    justify-content: center;
    text-align: center;
  }
  .wordmark {
    font-size: 30px;
    font-weight: 400;
    color: var(--ink);
    margin-bottom: 14px;
  }
  .name {
    font-size: 17px;
    font-weight: 700;
    letter-spacing: 2px;
  }
  .divider {
    width: 60px;
    height: 1px;
    background: var(--ink);
    margin: 9px 0 8px;
  }
  .titles {
    font-size: 8.5px;
    color: var(--muted);
    letter-spacing: .4px;
    margin-bottom: 7px;
  }
  .phone { font-size: 9px; color: var(--muted); margin-bottom: 3px; }
  .email { font-size: 11px; color: var(--teal); margin-bottom: 3px; }
  .web { font-size: 9px; color: var(--muted); }
  /* Back */
  .card-back .argyle {
    position: absolute;
    inset: 0;
    background: linear-gradient(135deg, var(--teal-soft) 0%, #e9ecea 45%, var(--teal) 100%);
  }
  .social {
    position: absolute;
    left: 180px;
    top: 48px;
    display: flex;
    align-items: center;
    gap: 8px;
  }
  .social-list {
    list-style: none;
    display: flex;
    flex-direction: column;
    gap: 22px;
  }
  .social-item {
    display: flex;
    align-items: center;
    gap: 8px;
    font-size: 11px;
    color: var(--ink);
  }
  .social-item .mark {
    width: 40px;
    height: 40px;
    background: var(--ink);
    border-radius: 4px;
  }
  .brace { width: 34px; height: 200px; }
  .handle {
    font-size: 22px;
    color: var(--ink);
  }
</style>
</head>
<body>
  <section class="card card-front">
    <svg class="frame" width="520" height="297" viewBox="0 0 520 297">
      <g fill="none" stroke="#222" stroke-width="1">
        <rect x="14" y="14" width="492" height="269"/>
        <rect x="20" y="20" width="480" height="257"/>
      </g>
      <g fill="#fff" stroke="#222" stroke-width="1">
        <rect x="12" y="12" width="10" height="10" transform="rotate(45 17 17)"/>
        <rect x="498" y="12" width="10" height="10" transform="rotate(45 503 17)"/>
        <rect x="12" y="275" width="10" height="10" transform="rotate(45 17 280)"/>
        <rect x="498" y="275" width="10" height="10" transform="rotate(45 503 280)"/>
      </g>
    </svg>
    <div class="content">
      <p class="wordmark">its Lena Corvel</p>
      <h1 class="name">LENA CORVEL</h1>
      <div class="divider"></div>
      <p class="titles">Brand Curator | Digital Storyteller | Social Entrepreneur</p>
      <p class="phone">240.555.0142</p>
      <p class="email">me@lenacorvel.com</p>
      <p class="web">www.itslenacorvel.com</p>
    </div>
  </section>

  <section class="card card-back">
    <div class="argyle" role="img" aria-label="Teal, grey and white argyle pattern with dashed stitch lines"></div>
    <div class="social">
      <ul class="social-list">
        <li class="social-item"><span class="mark"></span>Snapgrid</li>
        <li class="social-item"><span class="mark"></span>Friendly</li>
        <li class="social-item"><span class="mark"></span>Murmur</li>
      </ul>
      <svg class="brace" viewBox="0 0 34 200">
        <path d="M6 4 C22 4 14 70 16 92 C17 98 24 100 30 100 C24 100 17 102 16 108 C14 130 22 196 6 196" fill="none" stroke="#222" stroke-width="4" stroke-linecap="round"/>
      </svg>
      <p class="handle">@itslenacorvel</p>
    </div>
  </section>
</body>
</html>
```